Postcard Designs - Brenlow and Corvane

We are a locally owned, family operated pool service and repair company. The postcards we want to have designed is to co-market with two different companies (Brenlow and Corvane) . Both companies manufacture variable speed pumps. We are looking for customers who want to upgrade their systems to save $ on energy costs.

Both postcards are basically the same (and can use the same image rather than 2 different like I have in the Word doc). We just need to modify the text and company logo.

Postcard Specs

Full Bleed Size (starting document size)
8.64" x 5.59"
219 x 142 mm
2592 x 1677 pixels
* Finished artwork should use the full bleed dimensions for best results.
Document Trim Size (final size after being cut)
8.52" x 5.47"
216 x 139 mm
2556 x 1642 pixels
* Please be sure to keep all text within the safe margin.
Resolution
300 DPI

Target Market(s)

Adults in Northern California ages 30 - 80 that make the buying decisions for their families.

Industry/Entity Type

Pool Service

Font styles to use
Sans Serif

Colors
33a6d7
3277b5
acd037
fece3e

Requirements
Must have
• - company logo
- detail on variable speed pump
- cost savings chart
- image of family having fun (something related to the question on the front of the postcard - what would you do with $100/month?)

```html
<!DOCTYPE html>
<html lang="en">
<head>
<meta charset="utf-8">
<title>Brenlow Variable Speed Pump Postcard</title>
<link rel="stylesheet" href="https://fonts.googleapis.com/css2?family=Indie+Flower&family=PT+Sans:ital,wght@0,400;0,700;1,400&display=swap">
<style>
  :root{
    --sky:#33a6d7;
    --ocean:#3277b5;
    --lime:#acd037;
    --sun:#fece3e;
    --sun-soft:#fde48f;
    --paper:#ffffff;
    --stage:#eef1f4;
    --ink:#222a33;
    --grey-box:#f1f1f3;
    --green:#6dbb3a;
  }
  *{box-sizing:border-box;margin:0;padding:0}
  html,body{width:1200px;height:1000px;overflow:hidden;background:var(--stage)}
  .canvas{position:relative;width:1200px;height:1000px}
  .postcard{position:absolute;width:700px;height:450px;overflow:hidden;box-shadow:0 6px 18px rgba(0,0,0,.18)}
  .postcard--front{left:60px;top:30px;background:var(--ocean)}
  .postcard--back{left:440px;top:515px;background:var(--paper)}
  .layer{position:absolute;inset:0;width:100%;height:100%}
  .hand{font-family:"Indie Flower",cursive}

  /* front */
  .bubble{position:absolute;left:38px;top:62px;width:270px;height:150px;display:flex;align-items:center;justify-content:center;text-align:center;
    color:var(--ocean);font-size:27px;line-height:1.05;transform:rotate(-6deg);padding:0 18px}
  .front-tagline{position:absolute;right:26px;bottom:38px;width:380px;color:var(--paper);font-size:18px;line-height:1.1;text-align:right;transform:rotate(-5deg)}
  .brand-tag{position:absolute;left:24px;bottom:24px;display:flex;align-items:center;gap:6px;background:var(--paper);padding:4px 10px 4px 6px}
  .brand-tag__mark{width:14px;height:14px;background:var(--ocean)}
  .brand-tag__name{font-family:"PT Sans",sans-serif;font-weight:700;font-size:17px;color:var(--ocean);letter-spacing:.5px}

  /* back */
  .back-headline{position:absolute;right:22px;top:30px;width:470px;color:var(--ocean);font-size:23px;line-height:1.05;text-align:center}
  .savings{position:absolute;left:26px;top:70px;width:185px;font-family:"PT Sans",sans-serif}
  .savings__title{font-size:10px;font-weight:700;color:var(--ink)}
  .savings__big{display:flex;gap:10px;font-weight:700;color:var(--green);font-size:17px;margin-top:2px}
  .savings__big-labels{display:flex;gap:28px;font-size:6px;color:#666;margin-bottom:4px}
  .savings table{border-collapse:collapse;width:100%;font-size:6px;color:#666}
  .savings th{font-weight:400;text-align:center;padding:1px 2px}
  .savings td{padding:1px 2px;text-align:center}
  .savings td.value{color:var(--ocean);font-size:11px;font-weight:700}
  .savings td.label{text-align:left;width:60px}
  .savings__note{font-size:6px;font-style:italic;color:#444;margin-top:3px}
  .address-box{position:absolute;left:325px;top:125px;width:300px;height:170px;border-radius:18px;background:var(--grey-box);
    display:flex;align-items:center;justify-content:center;font-family:"PT Sans",sans-serif;font-size:9px;color:var(--ocean)}
  .disclaimer{position:absolute;left:26px;top:226px;width:285px;font-family:"PT Sans",sans-serif;font-style:italic;font-size:8.5px;line-height:1.3;color:var(--ink)}
  .cta{position:absolute;left:34px;top:318px;color:var(--ocean);font-size:15.5px;line-height:1.1;white-space:nowrap}
  .offer{position:absolute;left:40px;top:346px;width:620px;font-family:"PT Sans",sans-serif;font-size:10.5px;line-height:1.35;color:var(--ink)}
  .contact{position:absolute;left:40px;top:382px;font-family:"PT Sans",sans-serif;font-size:11px;color:var(--ink);display:flex;gap:24px}
</style>
</head>
<body>
<main class="canvas">

  <section class="postcard postcard--front" aria-label="Postcard front">
    <svg class="layer" viewBox="0 0 700 450" preserveAspectRatio="none">
      <defs>
        <linearGradient id="frontBg" x1="0" y1="0" x2="1" y2="1">
          <stop offset="0" stop-color="#33a6d7"/><stop offset="1" stop-color="#3277b5"/>
        </linearGradient>
        <linearGradient id="beachTone" x1="0" y1="0" x2="0" y2="1">
          <stop offset="0" stop-color="#bfe3f5"/><stop offset=".55" stop-color="#8fc9e6"/><stop offset="1" stop-color="#f3e2cf"/>
        </linearGradient>
      </defs>
      <rect width="700" height="450" fill="url(#frontBg)"/>
      <path d="M0 20 C180 -20 420 60 700 10 L700 0 L0 0Z" fill="#5fb8e0" opacity=".6"/>
      <path role="img" aria-label="Photo: happy family of four laughing on a sunny beach" fill="url(#beachTone)"
        d="M30 450 L30 200 C30 120 160 80 300 110 C420 135 520 120 600 150 C650 170 690 240 690 320 L690 450Z"/>
      <path d="M0 95 C150 30 300 140 470 60 S650 20 700 40" fill="none" stroke="#ffffff" stroke-width="3" opacity=".7"/>
      <path d="M140 40 C300 0 420 120 560 80 S660 0 700 -5" fill="none" stroke="var(--lime)" stroke-width="5"/>
      <path d="M0 395 C180 330 420 360 700 300 L700 450 L0 450Z" fill="var(--sky)" opacity=".9"/>
      <path d="M0 420 C200 380 400 420 700 360 L700 450 L0 450Z" fill="#4bb3df" opacity=".8"/>
      <path d="M52 70 C60 40 290 35 310 60 C330 90 320 190 290 200 C240 215 120 205 90 225 L95 205 C60 200 45 170 45 140Z" fill="var(--sun-soft)" opacity=".8" transform="translate(10 -8)"/>
      <path d="M52 70 C60 40 290 35 310 60 C330 90 320 190 290 200 C240 215 120 205 90 225 L95 205 C60 200 45 170 45 140Z" fill="var(--sun)"/>
    </svg>
    <h2 class="bubble hand">What would you do with… $100/month?</h2>
    <p class="front-tagline hand">Moving to a variable speed pump saves an average of $80 – $100/month on your energy bill.</p>
    <div class="brand-tag"><span class="brand-tag__mark"></span><span class="brand-tag__name">BRENLOW</span></div>
  </section>

  <section class="postcard postcard--back" aria-label="Postcard back">
    <svg class="layer" viewBox="0 0 700 450" preserveAspectRatio="none">
      <path d="M300 -14 C380 16 520 20 620 -6" fill="none" stroke="var(--lime)" stroke-width="6"/>
      <path d="M0 300 C40 290 80 300 90 330 C100 380 110 430 130 450 L0 450Z" fill="var(--sun)"/>
      <path d="M200 396 C320 300 520 290 700 335" fill="none" stroke="var(--lime)" stroke-width="3" opacity=".5"/>
      <path d="M0 430 L700 420 L700 450 L0 450Z" fill="var(--ocean)"/>
      <path d="M0 418 L700 410 L700 424 L0 432Z" fill="var(--sky)"/>
    </svg>
    <h2 class="back-headline hand">Trust only the best to upgrade your pool equipment! Marlow &amp; Sons is Sacramento's #1 rated pool service and repair company.</h2>

    <div class="savings">
      <p class="savings__title">Your Estimated Savings</p>
      <div class="savings__big"><span>$147</span><span>$1,764</span><span>95%</span></div>
      <div class="savings__big-labels"><span>Per Month</span><span>Per Season</span><span>Savings</span></div>
      <table>
        <tr><th></th><th>Variable Speed Pump</th><th>Single Speed Pump</th></tr>
        <tr><td class="label">Cost per season</td><td class="value">$84</td><td class="value">$1,848</td></tr>
        <tr><td class="label">Hours per day</td><td class="value">12</td><td class="value">8</td></tr>
        <tr><td class="label">Total horsepower</td><td class="value">1.0</td><td class="value">2.1</td></tr>
      </table>
      <p class="savings__note">Brenlow variable speed pump selected based on your pool size and location.</p>
    </div>

    <div class="address-box">Address &amp; Postage</div>

    <p class="disclaimer">Calculated energy savings are based on the selected speed only and System Curve C per California's Title 20 Appliance Energy Regulations. Operation at additional speeds may be required when using other equipment such as heaters, water features, etc. Actual savings may vary based on the single speed pump model and other hydraulic aspects such as plumbing size and length.</p>

    <p class="cta hand">Contact us within 30 days of receiving this postcard to schedule your Free Energy Audit</p>
    <p class="offer">In addition to the Free Energy Audit, if you decide to upgrade to a variable speed pump and you spend $1000 or more, we will also provide you with 1-month of pool cleaning service – FREE! Payment options are available.</p>
    <p class="contact"><span>916-555-0142</span><span>www.marlow-sons.com</span><span>info@marlow-sons.com</span></p>
  </section>

</main>
</body>
</html>
```